RVM Flooring Flyer/Direct Mail

I need a flyer that will be distributed by letterboxing. this flyer will be offering free measure and quotes for supply and installation of timber, bamboo, and laminate flooring. The flyer will need to eye catching and professional looking.
The main purpose of the flyer is to generate appointments that will be followed up by a sales measure and quote team.

- Free Measure and Quote
Services:
- Remove and dispose of old floor coverings
- Pre installation floor repair
- New floor installation
- Free dust and clean on every new floor installation

I have some design files, logo and stock images, the flyer must not clash with the logo and business card.

You can use any image from Pextra Images as I have subscription with them.
https://images.pextrafoto.com/au/gallery

Here are the links to the Timber and Bamboo flooring supplier that I will be buying from and the third link is for the laminate flooring supplier. Note, this is for getting an idea of what products we will be supplying and installing, Do not use their images!

https://www.grainhaven.com.au/timber-flooring/
https://cantorvex.com.au/bamboo-flooring/
http://www.dalvorsurfaces.com.au/brands/tenmark-laminate/

Target Market(s)

Domestic home owners

Industry/Entity Type

Construction Company

Colors

Designer to choose colors to be used in the design.

Requirements
Must have
• Size: A6 or DL
Nice to have
• Timber: Spotted Gum, Eastern States Blackbutt, Jarrah, Marri, and a large collection of French Oak.
• Bamboo: Our Bamboo range of flooring is engineered to withstand the extremes of the Australian climate.
• Laminate: All our laminate range comes with a 25 year product warranty. Choose from a large range of patterns, colours and finishes.

```html
<!DOCTYPE html>
<html lang="en">
<head>
<meta charset="utf-8">
<title>RVM Flooring Flyer</title>
<link href="https://fonts.googleapis.com/css2?family=Lato:wght@400;700&display=swap" rel="stylesheet">
<style>
  :root{
    --page:#7fa9a6;
    --charcoal:#3b3b3d;
    --charcoal-deep:#2e2e30;
    --panel-glass:rgba(40,40,44,.72);
    --stripe:#8a8a8c;
    --stripe-dark:#4a4a4c;
    --white:#ffffff;
    --paper:#f4f4f4;
    --wood-light:#e3b77e;
    --wood-mid:#c98a4a;
    --wood-dark:#9a5a2c;
  }
  *{box-sizing:border-box;margin:0;padding:0}
  html,body{width:720px;height:1200px;overflow:hidden}
  body{background:var(--page);font-family:"Lato",sans-serif;color:var(--white);position:relative}
  .flyer{position:absolute;left:40px;top:148px;width:640px;height:904px;background:var(--paper);overflow:hidden;box-shadow:0 8px 30px rgba(0,0,0,.25)}
  .hero-photo{position:absolute;left:0;top:0;width:600px;height:370px;border-bottom-left-radius:48px;
    background:linear-gradient(180deg,#dcdcdc 0%,#b9b9bb 35%,#9c9c9e 55%,#d9d8d6 75%,#c4c1bd 100%)}
  .hero-stripes{position:absolute;right:0;top:0;width:120px;height:370px}
  .brand-panel{position:absolute;left:53px;top:0;width:205px;height:251px;background:var(--panel-glass);border-bottom-left-radius:60px;border-bottom-right-radius:60px;display:flex;flex-direction:column;align-items:center;justify-content:center;gap:16px;padding-top:30px}
  .brand-mark{width:34px;height:34px;background:var(--white)}
  .brand-name{font-size:21px;font-weight:400;letter-spacing:2px;color:var(--white)}
  .services-band{position:absolute;left:0;top:381px;width:640px;height:162px;background:var(--charcoal);text-align:center}
  .services-title{font-size:18px;font-weight:700;line-height:24px;margin-top:10px}
  .services-title span{display:inline-block;border-bottom:2px solid var(--white);padding-bottom:1px}
  .services-list{list-style:none;margin-top:12px;font-size:14px;line-height:18px}
  .services-list li::before{content:"\2713\00a0"}
  .products{position:absolute;left:0;top:543px;width:640px;height:234px;background:linear-gradient(180deg,#f2f2f2,#dedede)}
  .product-card{position:absolute;top:10px;width:180px;height:206px;background:var(--charcoal);border:2px solid var(--white);border-radius:18px;overflow:hidden;box-shadow:0 0 0 2px var(--charcoal)}
  .product-card:nth-child(1){left:37px}
  .product-card:nth-child(2){left:233px}
  .product-card:nth-child(3){left:428px}
  .product-photo{height:103px;border-radius:0 0 14px 14px}
  .photo-timber{background:linear-gradient(160deg,#f5e3c4,var(--wood-light) 45%,var(--wood-mid))}
  .photo-bamboo{background:linear-gradient(180deg,#e8c48e,var(--wood-light) 50%,#d49d5c)}
  .photo-laminate{background:linear-gradient(170deg,var(--wood-dark),var(--wood-mid) 50%,#b0703a)}
  .product-name{font-size:14px;font-weight:700;text-align:center;margin-top:3px}
  .product-text{font-size:11.5px;line-height:13.5px;text-align:justify;padding:4px 10px 0}
  .contact{position:absolute;left:56px;top:777px;width:584px;height:127px;background:var(--charcoal);border-top-left-radius:30px;border-top-right-radius:40px}
  .contact-bars{position:absolute;left:0;top:790px;width:56px;height:114px}
  .contact-title{position:absolute;left:0;width:100%;top:10px;text-align:center;font-size:15px;font-weight:700}
  .contact-title span{border-bottom:2px solid var(--white);padding-bottom:1px}
  .contact-col{position:absolute;top:53px;list-style:none;font-size:14px;line-height:18px}
  .contact-col li{display:flex;align-items:center;gap:7px}
  .contact-col svg{width:12px;height:12px;flex:none}
  .col-left{left:26px}
  .col-right{left:314px}
  .divider{position:absolute;left:267px;top:48px;width:1px;height:64px;background:#8c8c8e}
  .indent{padding-left:19px}
</style>
</head>
<body>
<main class="flyer">
  <div class="hero-photo" role="img" aria-label="Modern open-plan dining room with pale timber floor, grey stone feature wall and fireplace"></div>
  <svg class="hero-stripes" viewBox="0 0 120 370" aria-hidden="true">
    <polygon points="120,0 120,60 40,370 0,370 0,360 90,0" fill="var(--white)"/>
    <polygon points="98,0 112,0 22,370 8,370" fill="var(--stripe)"/>
    <polygon points="120,20 120,80 50,370 34,370" fill="var(--stripe-dark)"/>
  </svg>
  <div class="brand-panel">
    <div class="brand-mark"></div>
    <div class="brand-name">RVM FLOORING</div>
  </div>

  <section class="services-band">
    <h1 class="services-title">Free Measure and Quote<br><span>Services:</span></h1>
    <ul class="services-list">
      <li>Remove and dispose of old floor coverings</li>
      <li>Pre installation floor repair</li>
      <li>New floor installation</li>
      <li>Free dust and clean on every new floor installation</li>
    </ul>
  </section>

  <section class="products">
    <article class="product-card">
      <div class="product-photo photo-timber" role="img" aria-label="Close-up of light timber floorboards"></div>
      <h2 class="product-name">Timber</h2>
      <p class="product-text">Spotted Gum, Eastern States Blackbutt, Jarrah, Marri, and a large collection of French Oak.</p>
    </article>
    <article class="product-card">
      <div class="product-photo photo-bamboo" role="img" aria-label="Close-up of bamboo flooring boards"></div>
      <h2 class="product-name">Bamboo</h2>
      <p class="product-text">Our Bamboo range of flooring is engineered to withstand the extremes of the Australian climate.</p>
    </article>
    <article class="product-card">
      <div class="product-photo photo-laminate" role="img" aria-label="Close-up of warm brown laminate flooring"></div>
      <h2 class="product-name">Laminate</h2>
      <p class="product-text">All our laminate range comes with a 25 year product warranty. Choose from a large range of patterns, colours and finishes.</p>
    </article>
  </section>

  <svg class="contact-bars" viewBox="0 0 56 114" aria-hidden="true">
    <polygon points="40,0 52,0 30,114 18,114" fill="var(--stripe)"/>
    <polygon points="24,20 34,20 16,114 6,114" fill="var(--stripe-dark)"/>
  </svg>
  <section class="contact">
    <h2 class="contact-title"><span>Contact Us</span></h2>
    <ul class="contact-col col-left">
      <li><svg viewBox="0 0 12 12"><circle cx="6" cy="6" r="6" fill="#fff"/><rect x="4" y="2.5" width="4" height="7" rx="1" fill="#3b3b3d"/></svg>0400 317 582</li>
      <li><svg viewBox="0 0 12 12"><circle cx="6" cy="6" r="6" fill="#fff"/><path d="M4 3l1.3 1.5-.7 1a4 4 0 0 0 1.9 1.9l1-.7L9 8l-1 1.2C5.6 9 3 6.4 2.8 4z" fill="#3b3b3d"/></svg>08 9306 4417</li>
      <li><svg viewBox="0 0 12 12"><circle cx="6" cy="6" r="6" fill="#fff"/><rect x="3" y="4" width="6" height="4" fill="#3b3b3d"/><path d="M3 4l3 2.2L9 4" stroke="#fff" stroke-width=".7" fill="none"/></svg>sam@RVMFlooring.com.au</li>
    </ul>
    <div class="divider"></div>
    <ul class="contact-col col-right">
      <li><svg viewBox="0 0 12 12"><circle cx="6" cy="6" r="6" fill="#fff"/><path d="M6 2.5a2.3 2.3 0 0 1 2.3 2.3C8.3 6.5 6 9.5 6 9.5S3.7 6.5 3.7 4.8A2.3 2.3 0 0 1 6 2.5z" fill="#3b3b3d"/><circle cx="6" cy="4.8" r=".9" fill="#fff"/></svg>42 Harlow Parade</li>
      <li class="indent">Westvale WA 6099</li>
      <li><svg viewBox="0 0 12 12"><circle cx="6" cy="6" r="6" fill="#fff"/><circle cx="6" cy="6" r="3.2" fill="none" stroke="#3b3b3d" stroke-width=".8"/><path d="M2.8 6h6.4M6 2.8c-1.6 1.8-1.6 4.6 0 6.4M6 2.8c1.6 1.8 1.6 4.6 0 6.4" stroke="#3b3b3d" stroke-width=".6" fill="none"/></svg>www.RVMFlooring.com.au</li>
    </ul>
  </section>
</main>
</body>
</html>
```